Keystone Homes/Real Estate valuation tool

We need a design for our our new Keystone Homes valuation tool.

The tool allows users to book a valuation of their house/property with the Keystone Homes, after they choose there property they can then complete their details and choose a booking time.

The mock up of the design we want is attached to this project.(Main Screen)

This also needs to be responsive so the design is easy to use on a mobile device.

Target Market(s)

estate agents

Industry/Entity Type

Keystone Homes

Number of Pages Required

1 page

Requirements
Must have
• Section 2 and 3 greyed out when user is on step 1
• Section 1 and 3 greyed out when user is on step 2
• Section 1 and 2 greyed out when the user is on step 3
• *** Design must be shown for mobile/ipad and desktop
Nice to have
• Clean and Simple
Should not have
• Dark colours

```html
<!DOCTYPE html>
<html lang="en">
<head>
<meta charset="utf-8">
<title>Keystone Homes – Book Your Valuation</title>
<link href="https://fonts.googleapis.com/css2?family=Lato:wght@400;700;900&family=Open+Sans:wght@400;700&family=Oswald:wght@500&family=Bitter:wght@400&display=swap" rel="stylesheet">
<style>
:root{
  --orange:#ffa21f;
  --orange-soft:#fde3bd;
  --orange-ring:#f7931e;
  --blue:#1f7ee8;
  --blue-dark:#1565c8;
  --sky-top:#1c8fe3;
  --sky-mid:#7cc3f2;
  --ground:#8da6a4;
  --ink:#333333;
  --ink-soft:#9a9a9a;
  --field-line:#c9c9c9;
  --field-bg:#f7f7f7;
  --tab-bg:#b9b9b9;
  --tab-active:#9e9e9e;
  --footer:#000000;
  --white:#ffffff;
}
*{box-sizing:border-box;margin:0;padding:0}
html,body{width:1200px;height:754px;overflow:hidden;background:var(--white)}
body{font-family:"Lato",sans-serif;color:var(--ink);position:relative}

.top-rule{position:absolute;left:0;top:0;width:1200px;height:3px;background:var(--orange)}
.site-header{position:absolute;left:0;top:3px;width:1200px;height:99px;background:var(--white)}
.brand{position:absolute;left:190px;top:30px;display:flex;align-items:center;gap:10px}
.brand-dot{width:28px;height:28px;border-radius:50%;background:var(--orange)}
.brand-name{font-family:"Lato",sans-serif;font-weight:900;font-size:22px;letter-spacing:1px;color:#1a1a1a}
.book-btn{position:absolute;left:771px;top:28px;width:234px;height:38px;background:var(--blue);border:1px solid var(--blue-dark);color:var(--white);display:flex;align-items:center;gap:10px;padding-left:10px;font-family:"Bitter",serif;font-size:14.5px}

.hero{position:absolute;left:0;top:102px;width:1200px;height:560px;background:linear-gradient(180deg,var(--sky-top) 0%,var(--sky-mid) 45%,#dfeef8 70%,var(--ground) 88%,#6f8a60 100%)}

.intro-bubble{position:absolute;left:224px;top:126px;width:752px;height:72px;background:linear-gradient(180deg,#ffffff,#f1f1f1);border-radius:36px;text-align:center;font-family:"Open Sans",sans-serif;font-size:19px;line-height:27px;color:#2a2a2a;padding-top:8px;box-shadow:0 1px 3px rgba(0,0,0,.15)}
.intro-bubble strong{font-weight:700}
.intro-bubble::after{content:"";position:absolute;left:380px;bottom:-20px;border-left:16px solid transparent;border-right:16px solid transparent;border-top:20px solid #f1f1f1}

.step-card{position:absolute;top:274px;width:262px;height:356px;background:var(--white);box-shadow:0 2px 6px rgba(0,0,0,.2)}
.step-card--one{left:190px}
.step-card--two{left:476px}
.step-card--three{left:760px}
.step-head{height:46px;background:var(--orange);color:var(--white);font-weight:700;font-size:16px;padding:16px 0 0 16px;letter-spacing:.2px}
.step-badge{position:absolute;right:-4px;top:-36px;width:50px;height:50px;border-radius:50%;background:var(--white);border:4px solid var(--orange-ring);font-family:"Oswald",sans-serif;font-weight:500;font-size:22px;color:#222;display:flex;align-items:center;justify-content:center}
.field-label{position:absolute;left:16px;font-size:12.5px}
.field{position:absolute;left:14px;width:234px;height:38px;border:1px solid var(--field-line);background:var(--field-bg);font-size:12.5px;padding:11px 10px}
.search-icon{position:absolute;right:0;top:0;width:36px;height:36px;border-left:1px solid var(--field-line);display:flex;align-items:center;justify-content:center}
.action-btn{position:absolute;left:13px;top:287px;width:235px;height:40px;background:var(--blue);border-bottom:2px solid var(--blue-dark);color:var(--white);font-weight:700;font-size:15px;text-align:center;line-height:40px}

.step-card--inactive .step-head{background:var(--orange-soft)}
.step-card--inactive .step-badge{border-color:var(--orange-ring)}
.step-card--inactive .field-label{color:var(--ink-soft)}
.step-card--inactive .field{color:#a8a8a8;background:#fbfbfb;border-color:#e6e6e6}
.step-card--inactive .action-btn{background:var(--orange-soft);border-bottom-color:#f3d3a4}

.day-tabs{position:absolute;left:13px;top:76px;width:239px;height:37px;display:flex;background:var(--tab-bg)}
.day-tab{flex:1;color:var(--white);font-size:7.5px;text-align:center;padding-top:8px;line-height:11px;border-right:1px solid #cfcfcf}
.day-tab:last-child{border-right:none}
.day-tab b{display:block;font-size:9.5px;font-weight:700}
.day-tab--today{flex:1.45;background:var(--tab-active)}
.slot{position:absolute;left:14px;width:235px;height:34px;border:1px solid #e6e6e6;display:flex;font-size:12px;color:#a8a8a8}
.slot-date{flex:1;padding:10px 10px}
.slot-time{width:51px;border-left:1px solid #e6e6e6;font-size:15px;text-align:center;padding-top:7px}

.site-footer{position:absolute;left:0;top:662px;width:1200px;height:92px;background:var(--footer);color:var(--white)}
.social-row{position:absolute;left:536px;top:17px;display:flex;gap:19px}
.social-dot{width:14px;height:14px;border-radius:50%;background:var(--white)}
.footer-rule{position:absolute;left:2px;top:47px;width:1196px;height:1px;background:#333}
.copyright{position:absolute;left:0;top:57px;width:1200px;text-align:center;font-size:12.5px}
</style>
</head>
<body>
<div class="top-rule"></div>
<header class="site-header">
  <div class="brand"><span class="brand-dot"></span><span class="brand-name">KEYSTONE HOMES</span></div>
  <a class="book-btn">
    <svg width="24" height="22" viewBox="0 0 24 22" aria-hidden="true"><rect x="1" y="3" width="22" height="18" rx="2" fill="none" stroke="#fff" stroke-width="2"/><rect x="1" y="3" width="22" height="5" fill="#fff"/><rect x="6" y="0" width="2" height="5" fill="#fff"/><rect x="16" y="0" width="2" height="5" fill="#fff"/><g fill="#fff"><rect x="5" y="10" width="3" height="3"/><rect x="10.5" y="10" width="3" height="3"/><rect x="16" y="10" width="3" height="3"/><rect x="5" y="15" width="3" height="3"/><rect x="10.5" y="15" width="3" height="3"/><rect x="16" y="15" width="3" height="3"/></g></svg>
    Book Your Valuation Online
  </a>
</header>

<div class="hero" role="img" aria-label="Blue sky over a softly blurred city skyline with trees"></div>

<div class="intro-bubble">
  Searching For Estate At The Cheapest Price And The Best Locations<br>
  Here's An Online App That Will Help You! <strong>Its Just A 3 Step Process</strong>
</div>

<section class="step-card step-card--one">
  <div class="step-head">YOUR PROPERTY DETAILS</div>
  <div class="step-badge">01</div>
  <div class="field-label" style="top:56px">Your Postcode</div>
  <div class="field" style="top:79px">2048 613920
    <span class="search-icon"><svg width="18" height="18" viewBox="0 0 18 18" aria-hidden="true"><circle cx="7" cy="7" r="5.5" fill="none" stroke="#333" stroke-width="2.2"/><line x1="11" y1="11" x2="16.5" y2="16.5" stroke="#333" stroke-width="2.8" stroke-linecap="round"/></svg></span>
  </div>
  <div class="field" style="top:129px">123 Street</div>
  <div class="field" style="top:180px">Test City</div>
  <div class="field" style="top:230px">Test Country</div>
  <div class="action-btn">PROCEED TO NEXT STEP</div>
</section>

<section class="step-card step-card--two step-card--inactive">
  <div class="step-head">YOUR PERSONAL DETAILS</div>
  <div class="step-badge">02</div>
  <div class="field-label" style="top:56px">Your Name</div>
  <div class="field" style="top:79px">Sam Carter</div>
  <div class="field-label" style="top:129px">Your Email Address</div>
  <div class="field" style="top:152px">sam23@mailbox.example</div>
  <div class="field-label" style="top:207px">Your Contact Number</div>
  <div class="field" style="top:227px">2048 613920</div>
  <div class="action-btn">PROCEED TO NEXT STEP</div>
</section>

<section class="step-card step-card--three step-card--inactive">
  <div class="step-head">APPOINTMENT DETAILS</div>
  <div class="step-badge">03</div>
  <div class="field-label" style="top:54px">Choose A Day For Appointment</div>
  <div class="day-tabs">
    <div class="day-tab day-tab--today">TODAY<b>01</b></div>
    <div class="day-tab" style="flex:1.3">TOMO<b>02</b></div>
    <div class="day-tab" style="flex:1.3">THUR<b>03</b></div>
    <div class="day-tab">FRI<b>04</b></div>
    <div class="day-tab">SAT<b>05</b></div>
    <div class="day-tab" style="flex:1.2">MON<b>07</b></div>
    <div class="day-tab" style="flex:1.2">TUE<b>08</b></div>
  </div>
  <div class="slot" style="top:118px"><span class="slot-date">Tuesday, 01 December</span><span class="slot-time">8:00</span></div>
  <div class="slot" style="top:157px"><span class="slot-date">Tuesday, 01 December</span><span class="slot-time">10:30</span></div>
  <div class="slot" style="top:196px"><span class="slot-date">Tuesday, 01 December</span><span class="slot-time">12:30</span></div>
  <div class="slot" style="top:236px"><span class="slot-date">Tuesday, 01 December</span><span class="slot-time">14:30</span></div>
  <div class="action-btn">CONFIRM APPOINTMENT</div>
</section>

<footer class="site-footer">
  <div class="social-row">
    <span class="social-dot" role="img" aria-label="Social link"></span>
    <span class="social-dot" role="img" aria-label="Social link"></span>
    <span class="social-dot" role="img" aria-label="Social link"></span>
    <span class="social-dot" role="img" aria-label="Social link"></span>
  </div>
  <div class="footer-rule"></div>
  <p class="copyright">Copyright 2015 Keystone Homes &nbsp;|&nbsp; All Rights Reserved.</p>
</footer>
</body>
</html>
```